One-Page Designed - Top 5 Tips for Curly Hair

I need a one-pager designed that looks friendly, informative, and natural, but that can be used as a PDF download for a website. the current website is not launched yet but the link is www.fernloftstudio.example for reference.

This piece will be the piece we send to clients once they log into our website and subscribe so it is a very important piece.

Fern Salon is an eco-friendly and holistically minded salon. Through research and education, we’ve curated a selection of less toxic hair color and hair styling products that offer professional results with the most natural ingredients on the market today. Whether you’re looking for a great haircut, expert grey coverage, bouncy curls or an amazing balayage, we’re here for you.

We’re dedicated to improving the locks of curly girls in the greater Boston area. We are curly hair experts who are committed to continuing education on the lasted curly hair cutting and coloring techniques. We’ll keep your curls healthy and fabulous with our carefully curated collection of products too.

Target Market(s)

Curly Hair Girls Who Want to Go to Natural Product Salon

Industry/Entity Type

Hair And Beauty

Font styles to use
Other font styles liked:
• Dancing Script and Arial Nova

Requirements
Must have
• Should have graphics that call out the tips and then have the blocks that go with them as the descriptions. Should be fun, friendly and informative. Final product should be send as a PDF.
• Colors should go with Hex: #5BC2E7 and Hex: #686A66 and Hex: #C8C9C7
• It should include their logo and a photo of the owner Marisol.
Nice to have
• Images that reflect the copy.

```html
<!DOCTYPE html>
<html lang="en">
<head>
<meta charset="utf-8">
<title>Top 5 Tips for Curly Hair – Fern Salon</title>
<link href="https://fonts.googleapis.com/css2?family=Dancing+Script:wght@700&family=Arimo:wght@400;700&display=swap" rel="stylesheet">
<style>
  :root {
    --sky: #5BC2E7;
    --deep: #1e96d6;
    --mid: #27a4de;
    --band-light: rgba(255,255,255,0.06);
    --white: #ffffff;
    --slate: #686A66;
    --stone: #C8C9C7;
    --ink: #3d3f3c;
  }
  * { margin: 0; padding: 0; box-sizing: border-box; }
  html, body { width: 927px; height: 1200px; overflow: hidden; }
  body { font-family: "Arimo", Arial, sans-serif; background: var(--white); }
  .page { position: relative; width: 927px; height: 1200px; overflow: hidden;
    background: linear-gradient(180deg, var(--deep) 0%, var(--mid) 60%, #2aa6df 100%); }

  .header-swoosh { position: absolute; left: 0; top: 0; width: 927px; height: 260px; }
  .title-top { position: absolute; left: 119px; top: 38px; color: var(--white);
    font-size: 45px; font-weight: 400; letter-spacing: 0; white-space: nowrap; }
  .title-script { position: absolute; left: 66px; top: 82px; color: var(--white);
    font-family: "Dancing Script", cursive; font-weight: 700; font-size: 116px; line-height: 1;
    white-space: nowrap; word-spacing: -14px; }
  .author-line { position: absolute; left: 298px; top: 210px; color: var(--white);
    font-size: 24px; letter-spacing: 2px; white-space: nowrap; }
  .header-divider { position: absolute; left: 563px; top: 52px; width: 1px; height: 162px; background: rgba(255,255,255,0.6); }
  .intro { position: absolute; left: 597px; top: 60px; width: 257px; color: var(--white);
    font-size: 14.5px; line-height: 22.4px; text-align: justify; }

  .backdrop-portrait { position: absolute; left: 520px; top: 410px; width: 407px; height: 655px;
    background: radial-gradient(ellipse at 55% 35%, rgba(120,210,240,0.45) 0%, rgba(90,190,235,0.25) 45%, rgba(40,160,220,0) 75%); }

  .tip { position: absolute; left: 0; width: 927px; }
  .tip.alt { background: var(--band-light); }
  .tip-photo { position: absolute; left: 88px; width: 195px; height: 130px; border: 1px solid rgba(255,255,255,0.85); }
  .tip-number { position: absolute; left: 59px; width: 58px; height: 58px; border-radius: 50%;
    background: var(--white); border: 4px solid var(--sky); color: var(--ink);
    font-size: 33px; font-weight: 700; display: flex; align-items: center; justify-content: center; }
  .tip-title { position: absolute; left: 302px; color: var(--white); font-size: 21px; font-weight: 700; letter-spacing: 1.4px; }
  .tip-body { position: absolute; left: 302px; width: 553px; color: var(--white);
    font-size: 11.6px; line-height: 18.6px; text-align: justify; }

  .footer { position: absolute; left: 0; top: 1066px; width: 927px; height: 134px; background: var(--white); }
  .owner-photo { position: absolute; left: 61px; top: 14px; width: 112px; height: 112px; border-radius: 50%;
    border: 5px solid var(--sky); background: radial-gradient(circle at 50% 45%, #b59582 0%, #6b4c3d 55%, #2e2622 100%); }
  .owner-name { position: absolute; left: 195px; top: 19px; color: var(--deep); font-size: 24px; font-weight: 400; letter-spacing: 2.4px; white-space: nowrap; }
  .owner-bio { position: absolute; left: 195px; top: 56px; width: 325px; color: var(--ink); font-size: 10px; line-height: 14.2px; }
  .footer-divider { position: absolute; left: 551px; top: 20px; width: 1px; height: 94px; background: var(--stone); }
  .salon-name { position: absolute; left: 588px; top: 30px; color: var(--sky); font-size: 40px; font-weight: 700; letter-spacing: 1px; white-space: nowrap; }
  .salon-url { position: absolute; left: 600px; top: 82px; color: var(--deep); font-size: 12.5px; letter-spacing: 2.2px; white-space: nowrap; }
</style>
</head>
<body>
<div class="page">
  <svg class="header-swoosh" viewBox="0 0 927 260" aria-hidden="true">
    <path d="M0 180 C 200 260, 420 220, 600 130 C 720 70, 850 40, 927 70 L927 0 L0 0 Z" fill="rgba(255,255,255,0.05)"/>
    <path d="M0 245 C 250 270, 500 200, 700 110 C 800 65, 880 60, 927 90 L927 100 C 860 80, 780 100, 690 140 C 480 235, 250 275, 0 255 Z" fill="rgba(255,255,255,0.08)"/>
  </svg>

  <div class="title-top">TOP 5 TIPS FOR</div>
  <div class="title-script">Curly Hair</div>
  <div class="author-line">Marisol Vantree</div>
  <div class="header-divider"></div>
  <p class="intro">I get it. Everyone is looking for ease and order in their busy lives. Whether you’ve just ditched your flat iron or you’re a long-time curly girl looking for fresh direction, here are our top tips for luscious curls and waves</p>

  <div class="backdrop-portrait" role="img" aria-label="Faint portrait of a woman with long curly hair"></div>

  <section class="tip" style="top:260px;height:151px;">
    <div class="tip-photo" role="img" aria-label="Close-up of long curly hair against a striped top" style="top:10px;background:linear-gradient(135deg,#8a5a36,#c49566 50%,#6b4428);"></div>
    <div class="tip-number" style="top:47px;">1</div>
    <h2 class="tip-title" style="top:14px;">CURL DIVERSITY</h2>
    <p class="tip-body" style="top:47px;">Embrace the diversity of your curls. Yes, you will have “curl diversity” everyday and that’s okay. Being consistent with your haircare routine and avoiding the temptation to blow dry or straighten will do wonders for your hair over the long term. I promise, your overall curl or wave pattern will improve over time. I also promise that you will never have the same head of curls twice. Variety is the spice of life!</p>
  </section>

  <section class="tip alt" style="top:411px;height:165px;">
    <div class="tip-photo" role="img" aria-label="Clear bottles of gentle cleanser standing in water" style="top:12px;background:linear-gradient(180deg,#bfe9f7,#6fcdec 70%,#2fa9d8);"></div>
    <div class="tip-number" style="top:47px;">2</div>
    <h2 class="tip-title" style="top:16px;">KEEP CLEANSER GENTLE</h2>
    <p class="tip-body" style="top:49px;">Keep your cleanser gentle and leave in a little bit of your conditioner. Using a cream based, no or low suds cleanser is the best way to insure you’re not stripping your hair of its natural oils. Once you’ve cleansed, condition and rinse very quickly, leaving a light amount of moisturizer in your hair. This provides a constant supply of the nourishment curls are always in need of. Apply your styling product right over your very wet, lightly conditioned curls and you’re all set.</p>
  </section>

  <section class="tip" style="top:576px;height:150px;">
    <div class="tip-photo" role="img" aria-label="Woman with curly hair partly wrapped in a silk scarf" style="top:12px;background:linear-gradient(90deg,#b9d3d8,#4a5a66 60%,#2a2a2e);"></div>
    <div class="tip-number" style="top:47px;">3</div>
    <h2 class="tip-title" style="top:14px;">REST EASY</h2>
    <p class="tip-body" style="top:46px;">Wrap your curls or waves in a silk scarf to avoid friction. If you’re rough sleeper and you wake up with your scarf wrapped somewhere between your neck and your armpit (me), a silk pillow case is a better and safer option. Less friction= smoother curls.</p>
  </section>

  <section class="tip alt" style="top:726px;height:175px;">
    <div class="tip-photo" role="img" aria-label="Two heads of long hair seen from behind, straight and curly" style="top:20px;left:85px;background:linear-gradient(90deg,#5a3a22,#a47a4e 50%,#6e4a2c);"></div>
    <div class="tip-number" style="top:56px;">4</div>
    <h2 class="tip-title" style="top:25px;">KEEP YOUR ENDS BLUNT</h2>
    <p class="tip-body" style="top:59px;">I’m not saying this because I’m a stylist, I swear. I’m saying this because I care about curly hair. Cutting curls every 6-10 weeks, depending on the length and curl type is essential to great hair health. Keeping your ends blunt and free of splits and frays will make styling easier and is especially important of you’re growing your hair longer. We all know how long that takes when you’re a curly girl.</p>
  </section>

  <section class="tip" style="top:901px;height:165px;">
    <div class="tip-photo" role="img" aria-label="Black bowl of cream conditioner with a tint brush" style="top:17px;left:84px;background:radial-gradient(circle at 40% 60%,#f3efe3 0%,#d9d4c6 30%,#2c2c2c 55%,#e6e6e6 80%);"></div>
    <div class="tip-number" style="top:53px;">5</div>
    <h2 class="tip-title" style="top:21px;">AVOID SILICONES AND SULFATES</h2>
    <p class="tip-body" style="top:55px;">You’ve heard this (pretty much everywhere) before but that’s only because it’s true. Silicones coat the hair and are extremely difficult to remove, leaving the hair with an altered texture and rendering it impervious to deep conditioning.&nbsp; Use only reputable hair care products like those from Willowleaf Botanics or Coilhaven. Beware of hidden silicones. They can be in the “fragrance” portion of the ingredient list.</p>
  </section>

  <footer class="footer">
    <div class="owner-photo" role="img" aria-label="Portrait photo of salon owner Marisol Vantree"></div>
    <h3 class="owner-name">MARISOL VANTREE</h3>
    <p class="owner-bio">Marisol is the owner of Fern Salon in Alderbrook and Fernwood, MA. She is a Ringlet advanced curly hair stylist and is certified in the Coil by Coil method. She is a curl advocate and a lover of natural and organic products.</p>
    <div class="footer-divider"></div>
    <div class="salon-name">FERN SALON</div>
    <div class="salon-url">www.fernloftstudio.example</div>
  </footer>
</div>
</body>
</html>
```